Maple Dental of Temecula needs a flyer

We need a flyer design for Maple Dental. We are located in the city of Temecula in California. Our dental office does general dentistry, cosmetic dentistry, dental implants, orthodontics, dental sleep apnea and TMJ treatment. We would like to design a flyer that could allow the reader know about our services and let them know that we accept new patients. We also have a new patient special that would included necessary dental x rays and dental exam for only $65. We do accept all major credit cards. Also our office accepts most PPO insurances. You can use some of the photos that are included or use stock photos of the dental procedure (they could be before/after photos).

```html
<!DOCTYPE html>
<html lang="en">
<head>
<meta charset="utf-8">
<title>Maple Dental – New Patient Flyer</title>
<link rel="stylesheet" href="https://fonts.googleapis.com/css2?family=Archivo+Black&family=Arimo:wght@400;700&family=Oswald:wght@500&family=Roboto:wght@400&display=swap">
<style>
  :root {
    --green: #0f6a12;
    --green-dark: #0a4d0c;
    --green-bright: #3a9a1c;
    --navy: #17467a;
    --navy-text: #1c356b;
    --star-blue: #1f72b8;
    --star-ring: #1a5f9e;
    --white: #ffffff;
    --ink: #1a1a1a;
  }
  * { box-sizing: border-box; margin: 0; padding: 0; }
  html, body { width: 848px; height: 1200px; overflow: hidden; background: var(--white); }
  .flyer { position: relative; width: 848px; height: 1200px; overflow: hidden; font-family: "Arimo", Arial, sans-serif; background: var(--white); }
  .backdrop { position: absolute; inset: 0; }

  .brand { position: absolute; left: 50px; top: 34px; color: var(--white); }
  .brand-name { font-family: "Arimo", sans-serif; font-weight: 700; font-size: 40px; line-height: 44px; }
  .brand-tagline { font-size: 13px; margin-top: 6px; }

  .badge { position: absolute; left: 32px; top: 140px; width: 216px; height: 216px; }
  .badge-spike { position: absolute; left: 31px; top: 31px; width: 154px; height: 154px; background: var(--star-blue); }
  .badge-core { position: absolute; left: 22px; top: 22px; width: 172px; height: 172px; border-radius: 50%; background: var(--star-blue); border: 3px solid var(--star-ring); }
  .badge-text { position: absolute; inset: 0; display: flex; flex-direction: column; align-items: center; justify-content: center; color: var(--white); font-weight: 700; text-align: center; line-height: 1; }
  .badge-big { font-size: 50px; letter-spacing: -1px; transform: scaleX(0.88); }
  .badge-small { font-size: 22px; transform: scaleX(0.9); margin: 1px 0 3px; }

  .offer { position: absolute; left: 74px; top: 488px; width: 336px; height: 306px; background: var(--green); border: 2px solid var(--green-dark); border-radius: 12px; box-shadow: 3px 3px 0 #06300a; color: var(--white); text-align: center; }
  .offer-lead { font-family: "Archivo Black", sans-serif; font-size: 31px; line-height: 37px; margin-top: 26px; letter-spacing: 1px; }
  .offer-price { font-family: "Archivo Black", sans-serif; font-size: 122px; line-height: 1; margin-top: 4px; letter-spacing: -2px; }

  .services { position: absolute; left: 436px; top: 486px; width: 338px; height: 308px; background: var(--green); border-radius: 12px; color: var(--white); padding: 22px 0 0 25px; }
  .services-title { font-family: "Oswald", sans-serif; font-weight: 500; font-size: 36px; line-height: 40px; letter-spacing: 0.5px; }
  .services-list { list-style: none; font-family: "Roboto", sans-serif; font-size: 29px; line-height: 35px; letter-spacing: 1px; margin-top: 8px; }
  .services-list li::before { content: "• "; font-size: 22px; }
  .services-list li.cont::before { content: ""; }
  .services-list li.cont { padding-left: 17px; }

  .doctor-photo { position: absolute; left: 34px; top: 818px; width: 108px; height: 138px; background: linear-gradient(180deg, #f2f2f2 0%, #c9b6a6 45%, #2b2b2f 75%, #1b1b1e 100%); }
  .doctor-name { position: absolute; left: 0; top: 959px; width: 186px; text-align: center; color: var(--navy-text); }
  .doctor-name strong { display: block; font-size: 12.5px; letter-spacing: 0.3px; }
  .doctor-name span { display: block; font-size: 11.5px; margin-top: 2px; }
  .about { position: absolute; left: 157px; top: 846px; width: 274px; color: var(--white); font-size: 11.4px; line-height: 12.8px; }

  .result { position: absolute; top: 822px; width: 186px; height: 122px; background: linear-gradient(180deg, #b07a6a 0%, #e8ddd2 45%, #f4efe8 55%, #b8705c 100%); }
  .result.before { left: 454px; }
  .result.after { left: 656px; }
  .result-label { position: absolute; left: 5px; bottom: -6px; background: var(--white); color: var(--navy-text); font-size: 16px; padding: 3px 12px 2px; }

  .ppo { position: absolute; left: 0; top: 1019px; width: 242px; height: 30px; background: var(--green-bright); clip-path: polygon(0 0, 100% 0, 93% 100%, 0 100%); color: var(--white); font-weight: 700; font-size: 12.5px; line-height: 30px; padding-left: 20px; }
  .phone { position: absolute; left: 254px; top: 970px; font-weight: 700; font-size: 84px; line-height: 96px; letter-spacing: -1px; color: var(--navy-text); white-space: nowrap; }
  .contact-bar { position: absolute; left: 6px; top: 1066px; width: 842px; height: 44px; background: var(--navy); clip-path: polygon(0 0, 100% 0, 100% 100%, 3% 100%); color: var(--white); font-size: 19.5px; line-height: 44px; padding-left: 60px; white-space: nowrap; }

  .cards { position: absolute; left: 38px; top: 1126px; }
  .cards-title { font-size: 10.5px; font-weight: 700; color: var(--ink); letter-spacing: 0.3px; }
  .cards-row { display: flex; gap: 2px; margin-top: 5px; }
  .card-name { width: 47px; height: 28px; border: 1px solid #c8c8c8; background: #f4f4f4; color: var(--navy-text); font-size: 10px; font-weight: 700; line-height: 26px; text-align: center; }
  .website { position: absolute; left: 300px; top: 1141px; font-size: 21px; font-weight: 700; color: var(--navy-text); }
  .social { position: absolute; left: 622px; top: 1126px; width: 200px; text-align: center; }
  .social-title { font-size: 12.5px; font-weight: 700; color: var(--navy-text); }
  .social-row { display: flex; justify-content: space-between; margin-top: 6px; }
  .social-link { width: 36px; height: 36px; border-radius: 50%; background: var(--star-blue); color: var(--white); font-size: 9px; font-weight: 700; line-height: 36px; text-align: center; }
</style>
</head>
<body>
<div class="flyer">
  <svg class="backdrop" width="848" height="1200" viewBox="0 0 848 1200">
    <defs>
      <linearGradient id="familyTone" x1="0" y1="0" x2="1" y2="1">
        <stop offset="0" stop-color="#dfe9d6"/>
        <stop offset="0.35" stop-color="#e8c4a8"/>
        <stop offset="0.7" stop-color="#f0d9c8"/>
        <stop offset="1" stop-color="#c9ccd2"/>
      </linearGradient>
    </defs>
    <path d="M290,0 H848 V450 C760,470 680,486 600,488 C500,470 400,430 290,380 Z" fill="url(#familyTone)" role="img" aria-label="Smiling family of four: father, mother, son and daughter"/>
    <path d="M0,305 C180,400 420,500 600,490 C700,485 780,462 848,440 V966 C620,946 380,940 0,952 Z" fill="var(--navy)"/>
    <path d="M150,944 C360,934 620,940 848,962 L848,968 C620,946 380,944 160,952 Z" fill="var(--green-bright)"/>
    <path d="M0,0 H372 C380,46 366,92 300,106 C210,122 90,128 0,142 Z" fill="var(--green)"/>
  </svg>

  <header class="brand">
    <div class="brand-name">Maple Dental</div>
    <div class="brand-tagline">Gentle Care for Every Smile!</div>
  </header>

  <div class="badge">
    <div class="badge-spike" style="transform:rotate(0deg)"></div>
    <div class="badge-spike" style="transform:rotate(15deg)"></div>
    <div class="badge-spike" style="transform:rotate(30deg)"></div>
    <div class="badge-spike" style="transform:rotate(45deg)"></div>
    <div class="badge-spike" style="transform:rotate(60deg)"></div>
    <div class="badge-spike" style="transform:rotate(75deg)"></div>
    <div class="badge-core"></div>
    <div class="badge-text">
      <span class="badge-big">NOW</span>
      <span class="badge-small">ACCEPTING</span>
      <span class="badge-big">NEW</span>
      <span class="badge-small">PATIENTS</span>
    </div>
  </div>

  <section class="offer">
    <p class="offer-lead">Dental X-Rays<br>&amp; Dental Exam<br>For Only</p>
    <p class="offer-price">$65</p>
  </section>

  <section class="services">
    <h2 class="services-title">DENTAL SERVICES:</h2>
    <ul class="services-list">
      <li>General Dentistry</li>
      <li>Cosmetic Dentistry</li>
      <li>Dental Implants</li>
      <li class="cont">Orthodontics</li>
      <li>Dental Sleep Apnea</li>
      <li>TMJ treatment</li>
    </ul>
  </section>

  <div class="doctor-photo" role="img" aria-label="Portrait of the dentist in a dark suit"></div>
  <div class="doctor-name"><strong>DANIEL HARROW</strong><span>DMD, MSD</span></div>
  <p class="about">The comprehensive dentistry services offered at Maple Dental and the experienced and friendly staff amount to a dental experience for our patients that is convenient and high quality. Our patients know they can rely on us for all their dental health needs.</p>

  <div class="result before" role="img" aria-label="Smile before treatment with gaps between teeth"><span class="result-label">BEFORE</span></div>
  <div class="result after" role="img" aria-label="Smile after cosmetic treatment"><span class="result-label">AFTER</span></div>

  <div class="ppo">We Accept Most PPO Insurances</div>
  <div class="phone">(555) 014-2268</div>
  <div class="contact-bar">41200 Vineyard Oak Road #118 Larkfield CA 90000 | office@maple-dental.com</div>

  <div class="cards">
    <div class="cards-title">ACCEPT ALL MAJOR CREDIT CARDS</div>
    <div class="cards-row">
      <span class="card-name">Paycard</span>
      <span class="card-name">Orbit</span>
      <span class="card-name">Summit</span>
      <span class="card-name">Nova</span>
    </div>
  </div>
  <div class="website">www.maple-dental.com</div>
  <div class="social">
    <div class="social-title">Follow Us/Patient Reviews:</div>
    <div class="social-row">
      <span class="social-link">Linkup</span>
      <span class="social-link">Circle</span>
      <span class="social-link">Buzz</span>
      <span class="social-link">Rate</span>
      <span class="social-link">Pics</span>
    </div>
  </div>
</div>
</body>
</html>
```